Homepage für Immobilienmakler
Zielgruppe
Wir sind ein neuer und junger Immobilienmakler. Wir wollen moderne und neue Wege gehen. Damit meinen wir, extrem modern und auffallend professionell.
Unsere Immobilien sind von Anlegerwohnungen über Häuser bis hin zu Gewerbeimmobilien
Unsere Zielgruppe ist von jung bis alt quer durch.
Aufgabenstellung
Homepagegestalltung für unsere Immobilienmaklerei.
Persönlich gefällt mir sehr gut das schwarz-weiß, jedoch wirkt das dann eher zu dunkel nehme ich mal an. Sonst würde mir die Homepage in grün, wie die Farbe im Logo, gut gefallen. Eventuell in weißer Schrift. ABER, ICH ÜBERLASSE EUCH DIE DESIGNSFARBEN.
Mir hätte dieses Design sehr gut gefallen, eventuelll könnt ihr dieses umgestallten:
http://vorlagenhain.example/item/auto-dealer-car-dealer-html-template/full_screen_preview/7719034
Kein muss, wenn ihr etwas besseres habt, dann bin ich auch froh ;)
Eventuell etwas mit Bewegung auf der Homepage oder so wäre auch gut.
Unsere Homepage hat die Domain:
wohnraum-kontor.example
Das Foto von mir sollte auf der Homepage eingebaut werden.
Auf der Homepage sollen die Immobilien, die wir verkaufen und vermieten angeführt werden. Zudem sollte ersichtlich sein, dass wir Immobilien suchen, um diese zu verkaufen oder zu vermieten.

```html
<!DOCTYPE html>
<html lang="de">
<head>
<meta charset="utf-8">
<title>Wohnraum Kontor – Immobilien</title>
<link rel="stylesheet" href="https://fonts.googleapis.com/css2?family=Open+Sans:ital,wght@0,400;0,600;0,700;1,400;1,600&family=PT+Sans+Narrow:wght@400;700&display=swap">
<style>
:root{
  --ink:#222;
  --text:#555;
  --muted:#888;
  --green:#3c9a3a;
  --black:#000;
  --bar:#333;
  --page:#eeeeee;
  --white:#fff;
  --line:#9a9a9a;
  --caption:rgba(30,30,30,.78);
}
*{box-sizing:border-box;margin:0;padding:0}
html,body{width:1024px;height:1200px;overflow:hidden}
body{position:relative;background:var(--page);font-family:"Open Sans",Arial,sans-serif;color:var(--text)}
.abs{position:absolute}

/* header */
.site-header{left:0;top:0;width:1024px;height:62px;background:linear-gradient(#fff,#ececec)}
.logo{font-family:"PT Sans Narrow","Arial Narrow",sans-serif;font-weight:700;color:var(--ink);display:flex;align-items:center;gap:5px;white-space:nowrap}
.logo .dot{width:12px;height:12px;border-radius:50%;background:var(--green)}
.header-logo{left:201px;top:13px;font-size:33px;line-height:40px}
.header-phone{left:491px;top:15px;font-size:13px;font-weight:700;color:#666;font-family:"PT Sans Narrow","Arial Narrow",sans-serif}
.header-address{left:491px;top:34px;font-size:8px;color:#777}
.social{display:flex;gap:3px}
.social span{width:22px;height:22px;border-radius:50%;background:radial-gradient(circle at 40% 35%,#f4f4f4,#9a9a9a);border:1px solid #888}
.header-social{left:752px;top:17px}

/* navigation */
.main-nav{left:0;top:62px;width:1024px;height:26px;background:var(--black)}
.main-nav a{position:absolute;top:5px;font-size:11.5px;color:var(--white);text-decoration:none}
.main-nav a.active{color:var(--green)}
.search-field{left:620px;top:5px;width:144px;height:16px;background:var(--white);border-radius:2px}
.search-btn{left:778px;top:4px;width:48px;height:18px;background:var(--white);font-size:10px;font-weight:700;color:var(--ink);text-align:center;line-height:18px}

/* hero */
.hero{left:203px;top:121px;width:334px;height:214px;background:linear-gradient(#7fb2e6 0%,#c9dcef 42%,#b9a98a 56%,#4f8aa8 70%,#2f6f94 100%)}
.hero-caption{left:0;bottom:0;width:100%;height:43px;background:var(--caption);color:var(--white)}
.hero-caption .title{left:8px;top:6px;font-size:14px;font-weight:700;font-family:"PT Sans Narrow","Arial Narrow",sans-serif}
.hero-caption .sub{left:8px;top:25px;font-size:7px;font-style:italic}
.hero-caption .price{left:277px;top:6px;font-size:14px;font-weight:700;font-family:"PT Sans Narrow","Arial Narrow",sans-serif}
.dots{left:271px;top:27px;display:flex;gap:4px}
.dots i{width:6px;height:6px;border-radius:50%;background:#ddd}

.search-panel{left:570px;top:121px;width:256px;height:214px;background:linear-gradient(#fff 0%,#dcdcdc 40%,#767676 100%);border-radius:3px}
.search-panel h2{position:absolute;left:11px;top:10px;font-size:13px;font-style:italic;font-weight:400;color:var(--ink)}
.field{position:absolute;height:17px;background:var(--white);border:1px solid #999;box-shadow:inset 0 1px 2px rgba(0,0,0,.25);font-size:7px;font-style:italic;color:#333;padding:3px 4px}
.field.select::after{content:"";position:absolute;right:4px;top:5px;border:4px solid transparent;border-top:5px solid #222}
.field.select::before{content:"";position:absolute;right:15px;top:1px;width:1px;height:13px;background:#555}
.submit{left:121px;top:183px;width:93px;height:17px;background:var(--black);color:var(--white);font-size:8px;font-style:italic;text-align:center;line-height:17px}

/* sections */
.section-title{font-family:"PT Sans Narrow","Arial Narrow",sans-serif;font-weight:700;font-size:13px;color:var(--ink)}
.rule{height:1px;background:var(--line)}
.arrows{display:flex;gap:3px}
.arrows span{width:12px;height:13px;background:var(--black);position:relative}
.arrows span::after{content:"";position:absolute;top:3px;border:4px solid transparent}
.arrows .prev::after{left:0;border-right:5px solid #fff}
.arrows .next::after{left:4px;border-left:5px solid #fff}

.card{position:absolute;top:392px;width:131px;height:105px}
.card .bar{position:absolute;left:0;bottom:0;width:100%;height:21px;background:var(--caption);color:var(--white);font-size:7px;font-weight:700;font-family:"PT Sans Narrow","Arial Narrow",sans-serif}
.card .bar b{position:absolute;top:6px}

.cta{position:absolute;top:528px;width:297px;height:51px;color:var(--white)}
.cta h3{position:absolute;left:46px;top:9px;font-size:14px;font-weight:700;font-family:"PT Sans Narrow","Arial Narrow",sans-serif}
.cta p{position:absolute;left:46px;top:26px;font-size:9px}
.cta .go{position:absolute;right:9px;top:12px;width:46px;height:24px;background:linear-gradient(#eee,#aaa);color:#333;font-size:7px;font-style:italic;line-height:9px;padding:2px 7px}
.cta svg{position:absolute;left:9px;top:11px}

.photo{position:absolute}
.photo .bar{position:absolute;left:0;bottom:0;width:100%;background:var(--caption);color:var(--white)}
.team .bar{height:29px}
.team .bar b{position:absolute;left:7px;top:2px;font-size:12px;font-family:"PT Sans Narrow","Arial Narrow",sans-serif}
.team .bar i{position:absolute;left:7px;top:18px;font-size:7px}
.info .bar{height:29px}
.info .bar b{position:absolute;left:4px;top:4px;font-size:8px;font-family:"PT Sans Narrow","Arial Narrow",sans-serif}
.info .bar i{position:absolute;left:4px;top:17px;font-size:7px}

/* footer */
.footer-info{left:0;top:912px;width:1024px;height:168px;background:linear-gradient(#fff,#f3f3f3);border-top:1px solid #aaa}
.footer-logo{left:203px;top:14px;font-size:27px;line-height:34px}
.footer-text{font-family:"PT Sans Narrow","Arial Narrow",sans-serif;font-size:13.5px;color:#666;line-height:17px}
.hours h4{font-family:"PT Sans Narrow","Arial Narrow",sans-serif;font-size:18px;font-weight:700;color:#666}
.map{left:703px;top:20px;width:120px;height:127px;background:var(--white);border:1px solid #ccc;padding:4px}
.map div{width:100%;height:100%;background:linear-gradient(135deg,#e9e3c9,#c9d6b2 50%,#b8cde4)}

.footer-bottom{left:0;top:1080px;width:1024px;height:120px;background:var(--black);border-top:3px solid #333}
.footer-col{position:absolute;top:8px}
.footer-col h5{font-weight:700;color:#ddd;text-decoration:underline;font-family:"PT Sans Narrow","Arial Narrow",sans-serif;font-size:13px;margin-bottom:2px}
.footer-col li{list-style:none;font-size:8.5px;font-style:italic;color:#ccc;line-height:14px}
</style>
</head>
<body>

<header class="abs site-header">
  <div class="abs logo header-logo">Wohnraum Kontor<span class="dot"></span></div>
  <div class="abs header-phone">Telefon: +(49) 301-7782</div>
  <div class="abs header-address">Lorem ipsum Dolor sit amet, 658 ,Consectetur, Adipisicing 56 D</div>
  <div class="abs social header-social"><span></span><span></span><span></span></div>
</header>

<nav class="abs main-nav">
  <a class="active" style="left:203px" href="#">Home</a>
  <a style="left:255px" href="#">Über uns</a>
  <a style="left:327px" href="#">Immobilien</a>
  <a style="left:410px" href="#">Leistungen</a>
  <a style="left:490px" href="#">Kontakt</a>
  <div class="abs search-field">
    <svg width="10" height="10" style="position:absolute;left:13px;top:3px" viewBox="0 0 10 10"><circle cx="4" cy="4" r="3" fill="none" stroke="#999" stroke-width="1.4"/><line x1="6.2" y1="6.2" x2="9" y2="9" stroke="#999" stroke-width="1.6"/></svg>
  </div>
  <div class="abs search-btn">Suchen</div>
</nav>

<section class="abs hero" role="img" aria-label="Stadtansicht mit Fluss, Kirchtürmen und Booten">
  <div class="abs hero-caption">
    <div class="abs title">Lorem Ipsum</div>
    <div class="abs sub">Lorem Ipsum &nbsp; Lorem Ipsum</div>
    <div class="abs price">Price</div>
    <div class="abs dots"><i></i><i></i><i></i><i></i></div>
  </div>
</section>

<form class="abs search-panel">
  <h2>Geben Sie hier Ihre Suchoptionen ein!</h2>
  <div class="field" style="left:12px;top:41px;width:203px">PLZ oder Ort oder Stadtteil</div>
  <div class="field select" style="left:12px;top:73px;width:203px">Objektart</div>
  <div class="field" style="left:12px;top:101px;width:92px">Zimmer ab</div>
  <div class="field" style="left:122px;top:101px;width:92px">Zimmer bis</div>
  <div class="field" style="left:12px;top:128px;width:92px">Größe (m²) ab</div>
  <div class="field" style="left:122px;top:128px;width:92px">Größe (m²) bis</div>
  <div class="field" style="left:12px;top:156px;width:92px">&nbsp;Preis (€) von</div>
  <div class="field" style="left:122px;top:156px;width:92px">&nbsp;Preis (€) bis</div>
  <div class="abs submit">Jetzt suchen!</div>
</form>

<h2 class="abs section-title" style="left:203px;top:356px">Aktuelle Immobilien</h2>
<div class="abs rule" style="left:203px;top:379px;width:623px"></div>
<div class="abs arrows" style="left:801px;top:361px"><span class="prev"></span><span class="next"></span></div>

<div class="card" style="left:203px;background:linear-gradient(#9bb8d8,#a88466 55%,#6d5a48)" role="img" aria-label="Mehrfamilienhaus mit Backsteinfassade"><div class="bar"><b style="left:6px">Lorem Ipsum</b><b style="left:96px">Price</b></div></div>
<div class="card" style="left:366px;background:linear-gradient(#b8c9dd,#8a6f5a 45%,#5d7a3e)" role="img" aria-label="Wohnanlage mit Bäumen im Innenhof"><div class="bar"><b style="left:6px">Lorem Ipsum</b><b style="left:96px">Price</b></div></div>
<div class="card" style="left:530px;background:linear-gradient(#8fb1d8,#e8e8e4 50%,#c9c9c4)" role="img" aria-label="Modernes weißes Gebäude"><div class="bar"><b style="left:6px">Lorem Ipsum</b><b style="left:96px">Price</b></div></div>
<div class="card" style="left:694px;background:linear-gradient(90deg,#e6e6e0,#9ccc7c 55%,#d8d8d4)" role="img" aria-label="Heller Innenraum mit grüner Wand und Treppe"><div class="bar"><b style="left:6px">Lorem Ipsum</b><b style="left:96px">Price</b></div></div>

<div class="cta" style="left:203px;background:var(--bar)">
  <svg width="28" height="28" viewBox="0 0 28 28"><circle cx="11" cy="11" r="8" fill="none" stroke="#fff" stroke-width="4"/><line x1="17" y1="17" x2="25" y2="25" stroke="#fff" stroke-width="5" stroke-linecap="round"/></svg>
  <h3>Sie suchen nach einer Immobilie?</h3>
  <p>Lorem Ipsum</p>
  <div class="go">Jetzt<br>suchen!</div>
</div>
<div class="cta" style="left:528px;background:var(--black)">
  <svg width="28" height="28" viewBox="0 0 28 28"><text x="3" y="24" font-size="26" font-weight="700" fill="#fff" font-family="Arial,sans-serif">€</text></svg>
  <h3>Sie verkaufen eine Immobilie?</h3>
  <p>Lorem Ipsum</p>
  <div class="go">Jetzt<br>verkaufen!</div>
</div>

<h2 class="abs section-title" style="left:203px;top:609px">Unser Team</h2>
<div class="abs rule" style="left:203px;top:632px;width:304px"></div>
<div class="abs arrows" style="left:478px;top:610px"><span class="prev"></span><span class="next"></span></div>

<h2 class="abs section-title" style="left:528px;top:609px">Aktuelle Informationen</h2>
<div class="abs rule" style="left:528px;top:632px;width:298px"></div>
<div class="abs arrows" style="left:798px;top:610px"><span class="prev"></span><span class="next"></span></div>

<div class="photo team" style="left:203px;top:645px;width:141px;height:222px;background:linear-gradient(#111,#2a2a2a)" role="img" aria-label="Porträt eines Immobilienmaklers vor dunklem Hintergrund"><div class="bar"><b>Lorem Ipsum</b><i>Immobilienmakler</i></div></div>
<div class="photo team" style="left:366px;top:645px;width:141px;height:222px;background:linear-gradient(#fafafa,#e9e9e9)" role="img" aria-label="Porträt einer Immobilienmaklerin vor hellem Hintergrund"><div class="bar"><b>Lorem Ipsum</b><i>Immobilienmakler</i></div></div>

<div class="photo info" style="left:528px;top:645px;width:133px;height:104px;background:linear-gradient(#9ec0e0,#dcd6c4 50%,#8fa58a)" role="img" aria-label="Wohnblock mit bunten Balkonen"><div class="bar"><b>Wohnmarkt Journal</b><i>Längste Immobilienboomphase der...</i></div></div>
<div class="photo info" style="left:693px;top:645px;width:133px;height:104px;background:linear-gradient(#c8c8c8,#a89484 50%,#8a8078)" role="img" aria-label="Straßenszene mit Zetteln an einem Laternenpfahl"><div class="bar"><b>Wohnkosten im Vergleich</b><i>Wie teuer Wohnen wirklich ist</i></div></div>
<div class="photo info" style="left:528px;top:763px;width:133px;height:104px;background:linear-gradient(135deg,#c7d6ea,#8ea4c4)" role="img" aria-label="Illustration eines Steckers"><div class="bar"><b>Ratgeber Energiesparen</b><i>Energie und Geld sparen</i></div></div>
<div class="photo info" style="left:693px;top:763px;width:133px;height:104px;background:linear-gradient(#e4e4dc,#b4b4ac)" role="img" aria-label="Aushang einer Wohnungssuche"><div class="bar"><b>Wohnpreisspiegel 2013/2014</b><i>Mieterwahnsinn? Alles Quatsch!</i></div></div>

<footer>
  <div class="abs footer-info">
    <div class="abs logo footer-logo">Wohnraum Kontor<span class="dot" style="width:10px;height:10px"></span></div>
    <div class="abs footer-text" style="left:203px;top:54px">Lorem ipsum Dolor sit amet, 658<br>Consectetur, Adipisicing 56 D</div>
    <div class="abs footer-text" style="left:203px;top:99px">Telefon: +(49) 301-7782<br>FAX: &nbsp;&nbsp;&nbsp;&nbsp;+(49) 301-7783</div>
    <div class="abs footer-text" style="left:203px;top:137px">Email: post@wohnraum-kontor.example</div>
    <div class="abs hours" style="left:446px;top:54px"><h4>Öffnungszeiten</h4></div>
    <div class="abs footer-text" style="left:446px;top:89px;line-height:21px">Montag-Freitag: &nbsp;9:00- 17:00 Uhr<br>Samstags: 9:00- 14:00 Uhr</div>
    <div class="abs map"><div role="img" aria-label="Stadtplan mit Standortmarkierung"></div></div>
  </div>
  <div class="abs footer-bottom">
    <div class="footer-col" style="left:202px"><h5>Site Map</h5><ul><li>Home</li><li>Über uns</li><li>Immobilien</li><li>Leistungen</li><li>Kontakt</li><li>Impressum</li></ul></div>
    <div class="footer-col" style="left:358px"><h5>Sie brauchen Hilfe</h5><ul><li>Lorem Ipsum</li><li>Lorem Ipsum</li><li>Lorem Ipsum</li></ul></div>
    <div class="footer-col" style="left:529px"><h5>Login User</h5><ul><li>Lorem Ipsum</li><li>Lorem Ipsum</li><li>Lorem Ipsum</li></ul></div>
    <div class="footer-col" style="left:699px"><h5>Finde uns auf</h5></div>
    <div class="abs social" style="left:698px;top:41px"><span></span><span></span><span></span></div>
  </div>
</footer>

</body>
</html>
```